Sports coaching website.

Hi there web designers,

We need a modern fully functional website to set us apart from our competition. The website will be information based with pictures and videos provided by us. The website must include members log in where they can pay for sessions directly online and subscribe to direct debit.

Target Market(s)

parents/teachers/schools/community/children.

Number of Pages Required

5+ page

Font styles to use
Sans Serif

Colors
acd037
3176b5
ffffff
000000
919191
f37122

Requirements
Must have
• Pictures, be modern, fully functional, must be clear, bold, e-basket, log-in.

```html
<!DOCTYPE html>
<html lang="en">
<head>
<meta charset="utf-8">
<title>Field Forge Sports</title>
<link href="https://fonts.googleapis.com/css2?family=Roboto:wght@400;500;700&family=Open+Sans:ital,wght@0,400;0,600;1,400&display=swap" rel="stylesheet">
<style>
:root{
  --orange:#f37122;
  --orange-dark:#d9520f;
  --lime:#e0f645;
  --lime-btn:#d6f03c;
  --grass:#1f3d14;
  --white:#ffffff;
  --black:#000000;
  --grey:#919191;
  --text:#555555;
  --footer:#2b2b2b;
  --footer-bottom:#1e1e1e;
  --red-deep:#7c1410;
}
*{margin:0;padding:0;box-sizing:border-box}
html,body{width:1200px;height:2748px;overflow:hidden}
body{position:relative;background:var(--white);font-family:'Open Sans',sans-serif;color:var(--text)}
.abs{position:absolute}
.brand{position:absolute;font-family:'Roboto',sans-serif;font-weight:700;text-transform:uppercase;display:flex;align-items:center;gap:10px}
.brand .mark{width:22px;height:22px;border-radius:50%}

/* header */
.site-header{left:0;top:0;width:1200px;height:160px;background:var(--white)}
.site-header .brand{left:0;width:1200px;top:58px;justify-content:center;font-size:34px;color:var(--black)}
.site-header .brand .mark{background:var(--orange)}
.main-nav{left:0;top:160px;width:1200px;height:52px;background:linear-gradient(#f8883a,#e5560e);display:flex;padding-left:128px}
.main-nav a{font-family:'Roboto',sans-serif;font-size:17px;color:var(--white);text-decoration:none;text-transform:uppercase;padding:0 18px;line-height:52px;border-right:1px solid rgba(255,255,255,.25)}
.main-nav a.active{background:rgba(170,50,0,.35)}

/* hero */
.hero{left:0;top:212px;width:1200px;height:415px;background:radial-gradient(circle at 50% 50%,#3b6a25,var(--grass) 80%)}
.hero-title{left:141px;top:103px;font-family:'Roboto',sans-serif;font-size:40px;color:var(--white);font-weight:500}
.hero-sub{left:141px;top:154px;font-family:'Roboto',sans-serif;font-size:24px;color:var(--white);font-weight:500}
.hero-text{left:141px;top:194px;width:420px;font-size:14px;line-height:21px;color:var(--white)}
.dots{display:flex;gap:7px}
.dots span{width:17px;height:17px;border-radius:50%;background:var(--white)}
.dots span.hollow{background:none;border:2px solid var(--white)}
.hero .dots{left:141px;top:253px}
.video{left:614px;top:72px;width:417px;height:256px;border:3px solid #dcdcdc;background:linear-gradient(135deg,#b9a28c,#6f6254)}
.video-bar{left:0;bottom:0;width:100%;height:26px;background:#1c1c1c}

/* what we do */
.section-title{position:absolute;left:0;width:1200px;text-align:center;font-family:'Roboto',sans-serif;text-transform:uppercase}
.about-title{top:670px;font-size:30px;color:#444}
.about-lead{left:170px;top:720px;width:860px;text-align:center;font-size:15.5px;line-height:28px;color:var(--grey)}
.about-body{left:170px;top:790px;width:860px;text-align:center;font-size:13.5px;line-height:27px;color:var(--grey)}

/* gallery */
.gallery-band{left:0;top:925px;width:1200px;height:340px}
.gallery-title{top:958px;font-size:27px;color:#7a4a00}
.gallery-item{top:1015px;width:216px;height:135px;background:linear-gradient(135deg,#7d8a6a,#a98f6d)}

/* training */
.training-photo{left:0;top:1202px;width:1200px;height:456px;background:linear-gradient(135deg,#6f6a5e,#b88a5a)}
.training-panel{left:590px;top:1202px;width:610px;height:456px;background:rgba(243,113,34,.82)}
.training-kicker{left:641px;top:1340px;font-family:'Roboto',sans-serif;font-size:28px;color:var(--white);text-transform:uppercase}
.training-title{left:641px;top:1374px;font-family:'Roboto',sans-serif;font-size:39px;font-weight:500;color:var(--white);text-transform:uppercase}
.training-text{left:643px;top:1430px;width:400px;font-size:14.5px;line-height:23px;color:var(--white)}
.btn-outline{left:645px;top:1519px;width:125px;height:37px;border:2px solid var(--white);color:var(--white);font-family:'Roboto',sans-serif;font-size:15px;font-weight:500;text-align:center;line-height:33px}

/* events */
.events-title{top:1703px;font-size:24px;color:var(--orange-dark)}
.event{top:1762px;width:271px}
.event-photo{width:271px;height:147px}
.event h3{margin-top:12px;font-size:15.5px;font-weight:400;color:#333}
.event p{margin-top:6px;font-size:11.5px;line-height:20px;color:var(--grey)}
.event a{display:block;margin-top:2px;font-family:'Roboto',sans-serif;font-size:11.5px;font-weight:700;color:var(--orange-dark);text-decoration:none}
.btn-booking{left:506px;top:2043px;width:192px;height:46px;border-radius:23px;background:var(--lime-btn);font-family:'Roboto',sans-serif;font-size:15.5px;font-weight:500;color:#222;text-align:center;line-height:46px}

/* testimonials */
.testimonials{left:0;top:2134px;width:1200px;height:299px;background:linear-gradient(110deg,var(--red-deep) 10%,#b8300f 55%,var(--orange-dark))}
.testi-title{top:50px;font-size:24px;color:var(--white);font-weight:500}
.avatar{left:206px;top:126px;width:90px;height:90px;border-radius:50%;border:4px solid var(--white);background:linear-gradient(#8a5a44,#d8b49b)}
.testi-name{left:311px;top:152px;font-family:'Roboto',sans-serif;font-size:14px;font-weight:500;color:var(--white);text-transform:uppercase}
.testi-loc{left:311px;top:177px;font-size:12px;color:var(--white)}
.testi-divider{left:489px;top:104px;width:1px;height:128px;background:rgba(255,255,255,.4)}
.testi-quote{left:528px;top:127px;width:520px;font-size:13.5px;line-height:29px;font-style:italic;color:var(--white)}
.testi-quote .q{font-family:'Roboto',sans-serif;font-size:28px;font-style:normal;vertical-align:-6px}
.testimonials .dots{left:560px;top:255px}

/* footer */
.site-footer{left:0;top:2433px;width:1200px;height:260px;background:var(--footer)}
.footer-col{top:42px}
.footer-col h4{font-family:'Roboto',sans-serif;font-size:20px;font-weight:400;color:var(--lime)}
.footer-col ul{list-style:none;margin-top:14px}
.footer-col li{font-size:12.5px;color:#cfcfcf;line-height:28px}
.site-footer .brand{left:898px;top:115px;font-size:22px;color:var(--white)}
.site-footer .brand .mark{background:var(--orange)}
.socials{left:660px;top:196px;display:flex;gap:18px}
.socials span{width:28px;height:28px;border-radius:50%;background:#3c3c3c}
.footer-bottom{left:0;top:2693px;width:1200px;height:55px;background:var(--footer-bottom);text-align:center;line-height:55px;font-size:11.5px;color:#777}
</style>
</head>
<body>

<header class="site-header abs">
  <div class="brand"><span class="mark"></span>Field Forge Sports</div>
</header>

<nav class="main-nav abs">
  <a class="active">Home Page</a><a>About FFS</a><a>Schools</a><a>Sessions</a><a>Workshops</a><a>Charity/Community</a><a>Contact</a>
</nav>

<section class="hero abs" role="img" aria-label="Close-up of green artificial turf">
  <h1 class="hero-title abs">SPORTS &amp; TRAINING</h1>
  <p class="hero-sub abs">MORBI DIAM MAURIS VIVERRA</p>
  <p class="hero-text abs">dui aliquet felis at cursus magna nisl nec elit Praesent elementum elit at tellus nec ultricies sit</p>
  <div class="dots abs"><span class="hollow"></span><span></span><span></span><span></span></div>
  <div class="video abs" role="img" aria-label="Video of children sitting on a sports hall floor">
    <svg class="abs" style="left:170px;top:82px" width="66" height="66" viewBox="0 0 66 66"><circle cx="33" cy="33" r="30" fill="rgba(255,255,255,.25)" stroke="#fff" stroke-width="3"/><path d="M26 20 L48 33 L26 46 Z" fill="#fff"/></svg>
    <div class="video-bar abs">
      <svg width="411" height="26" viewBox="0 0 411 26"><path d="M9 8 L17 13 L9 18 Z" fill="#fff"/><rect x="28" y="11" width="255" height="4" rx="2" fill="#555"/><rect x="28" y="11" width="120" height="4" rx="2" fill="#3176b5"/><path d="M382 10 h4 l5 -4 v14 l-5 -4 h-4 Z" fill="#fff"/></svg>
    </div>
  </div>
</section>

<section class="about">
  <h2 class="section-title about-title">What We Do</h2>
  <p class="about-lead abs">Clearfield &amp; Harbor eleifend libero a tempus libero lectus feugiat felis Morbi diam mauris viverra in gravida eu mattis in ante Morbi eget arcu Morbi porta libero id ullamcorper nonummy nibh</p>
  <p class="about-body abs">ligula pulvinar metus eget consectetuer augue nisi quis lacus Ut ac mi quis lacus mollis aliquam Curabitur iaculis tempus eros Curabitur vel mi sit amet magna malesuada ultrices Ut nisi erat fermentum vel congue id euismod in elit Fusce ultricies orci ac feugiat suscipit leo massa sodales velit et scelerisque mi tortor at ipsum cligula augue bibendum</p>
</section>

<section class="training">
  <div class="training-photo abs" role="img" aria-label="Child batting at a cricket wicket in an indoor sports hall"></div>
  <div class="training-panel abs"></div>
  <svg class="gallery-band abs" width="1200" height="340" viewBox="0 0 1200 340"><polygon points="0,0 1200,0 1200,277 590,337 0,277" fill="var(--lime)"/></svg>
  <p class="training-kicker abs">We Give Training</p>
  <p class="training-title abs">From Professional</p>
  <p class="training-text abs">Aommodo a mi Morbi ornare gravida elit Integer congue augue et malesuada iaculis ipsum dui aliquet felis at cursus magna nisl nec elit Praesent</p>
  <div class="btn-outline abs">Learn More</div>
</section>

<section class="gallery">
  <h2 class="section-title gallery-title">Our Gallery</h2>
  <div class="gallery-item abs" style="left:143px" role="img" aria-label="Child dribbling a ball on an outdoor pitch"></div>
  <div class="gallery-item abs" style="left:376px" role="img" aria-label="Group of children seated in a sports hall"></div>
  <div class="gallery-item abs" style="left:608px" role="img" aria-label="Children holding footballs indoors"></div>
  <div class="gallery-item abs" style="left:841px" role="img" aria-label="Children playing football in a hall"></div>
</section>

<section class="events">
  <h2 class="section-title events-title">Upcoming Events</h2>
  <article class="event abs" style="left:154px">
    <div class="event-photo" role="img" aria-label="Fan in team colours holding a football" style="background:linear-gradient(135deg,#3a5ab0,#e8e8e8 55%,#c8333a)"></div>
    <h3>Cum sociis natoque penatibus</h3>
    <p>et magnis dis parturient montes nascetur ridic ulus mus In iaculis facilisis</p>
    <a>READ MORE</a>
  </article>
  <article class="event abs" style="left:462px">
    <div class="event-photo" role="img" aria-label="Children training in a large sports hall" style="background:linear-gradient(#5a5550,#b89f7e)"></div>
    <h3>Donec dictum lectus non</h3>
    <p>et magnis dis parturient montes nascetur ridic ulus mus In iaculis facilisis</p>
    <a>READ MORE</a>
  </article>
  <article class="event abs" style="left:775px">
    <div class="event-photo" role="img" aria-label="Young supporters holding up a flag" style="background:linear-gradient(#3d3d3d,#c23a2a 50%,#e3b62c)"></div>
    <h3>Praesent elementum elit at tellus</h3>
    <p>et magnis dis parturient montes nascetur ridic ulus mus In iaculis facilisis</p>
    <a>READ MORE</a>
  </article>
  <div class="btn-booking abs">Booking Information</div>
</section>

<section class="testimonials abs">
  <svg class="abs" style="left:582px;top:0" width="36" height="19" viewBox="0 0 36 19"><polygon points="0,0 36,0 18,19" fill="var(--white)"/></svg>
  <h2 class="section-title testi-title">Testimonials</h2>
  <div class="avatar abs" role="img" aria-label="Portrait of the reviewer"></div>
  <p class="testi-name abs">Clara Benton</p>
  <p class="testi-loc abs">City Location Area</p>
  <div class="testi-divider abs"></div>
  <p class="testi-quote abs"><span class="q">“</span> Cras a ante vitae enim iaculis aliquam Mauris nunc quam venenatis nec euismod sit amet egestas placerat est Pellentesque habitant morbi tristique senectus et netus et malesuada fames ac turpis egestas <span class="q">”</span></p>
  <div class="dots abs"><span class="hollow"></span><span></span><span></span><span></span></div>
</section>

<footer class="site-footer abs">
  <div class="footer-col abs" style="left:123px"><h4>Quick Links</h4><ul><li>Home Page</li><li>About FFS</li><li>Schools</li><li>Sessions</li></ul></div>
  <div class="footer-col abs" style="left:302px"><h4>Links</h4><ul><li>Workshops</li><li>Charity/Community</li><li>Contact</li></ul></div>
  <div class="footer-col abs" style="left:478px"><h4>Resources</h4><ul><li>Videos</li><li>Blogs</li><li>Upcoming Events</li><li>Sitemap</li></ul></div>
  <div class="footer-col abs" style="left:660px"><h4>Contact Us</h4><ul><li>418 Meadowbrook Lane Suite B12</li><li>Ashford, PA 19320</li><li>(555) 014-2287</li><li>hello@fieldforge.example</li></ul></div>
  <div class="socials abs"><span></span><span></span><span></span><span></span></div>
  <div class="brand"><span class="mark"></span>Field Forge Sports</div>
</footer>

<div class="footer-bottom abs">© 2016 Field Forge Sports &nbsp;All right reserved &nbsp;Term of Use</div>

</body>
</html>
```